Facebook Add for Copper Kettle

We need an add designed for our seasonal restaurant that we can post on face book to announce that we are open for the 2016 season. We want it to be something that they can like and share on face book, and then print off and bring in during the month of march to receive a discount. Would prefer a add showcasing food, but not apposed to using the buiding. We want the offer to be $10 off second entree during march. Website is thecopperkettlegrillhouse.example 555-213-8967
Open Friday and Saturday night 5-9 March thru October. Lunch on Saturdays only 12-3.

Industry/Entity Type

Restaurant

```html
<!DOCTYPE html>
<html lang="en">
<head>
<meta charset="utf-8">
<title>Copper Kettle – Season Opening Cover</title>
<link rel="stylesheet" href="https://fonts.googleapis.com/css2?family=Fjalla+One&family=Montserrat:wght@500&display=swap">
<style>
  :root {
    --page-bg: #e9ebf0;
    --ink: #1f1f1f;
    --accent-red: #c23a26;
    --offer-red: rgba(190, 52, 34, 0.92);
    --panel-white: rgba(255, 255, 255, 0.82);
    --white: #ffffff;
    --meat-dark: #3b2a22;
    --meat-mid: #6b4b3c;
    --plate: #f4f2ee;
    --greens: #8fb06a;
  }
  * { margin: 0; padding: 0; box-sizing: border-box; }
  html, body { width: 1200px; height: 603px; overflow: hidden; }
  body { background: var(--page-bg); position: relative; font-family: "Fjalla One", "Arial Narrow", sans-serif; color: var(--ink); }

  .cover { position: absolute; left: 50px; top: 80px; width: 1100px; height: 407px; overflow: hidden; background: var(--plate); }

  .food-photo {
    position: absolute; left: 0; top: 0; width: 100%; height: 100%;
    background:
      radial-gradient(ellipse 320px 230px at 640px 230px, var(--meat-mid) 0%, var(--meat-dark) 70%, rgba(59,42,34,0) 100%),
      radial-gradient(ellipse 200px 90px at 960px 60px, var(--greens) 0%, rgba(143,176,106,0) 100%),
      linear-gradient(120deg, #f7f5f1 0%, #ebe6df 45%, #f3f1ed 100%);
  }

  .hours-panel { position: absolute; left: 0; top: 0; width: 304px; height: 100%; background: var(--panel-white); }
  .contact-panel { position: absolute; right: 0; top: 0; width: 200px; height: 100%; background: linear-gradient(90deg, rgba(255,255,255,0) 0%, var(--panel-white) 30%); }

  .season-title { position: absolute; left: 39px; top: 28px; font-size: 26px; line-height: 1; }
  .season-months { position: absolute; left: 39px; top: 64px; font-size: 21px; color: var(--accent-red); line-height: 1; }
  .hours-block { position: absolute; left: 39px; font-size: 15px; line-height: 1.45; text-transform: uppercase; }
  .hours-block .time { font-size: 14px; }
  .hours-night { top: 120px; }
  .hours-lunch { top: 170px; }

  .offer-tag {
    position: absolute; left: 457px; top: 204px; height: 40px; padding: 0 8px;
    background: var(--offer-red); color: var(--white); font-size: 19px; line-height: 40px;
  }

  .contact-line { position: absolute; left: 931px; display: flex; align-items: flex-start; gap: 8px; font-size: 22px; line-height: 27px; }
  .contact-phone { top: 50px; }
  .contact-address { top: 102px; }
  .contact-line svg { flex: none; margin-top: 1px; }

  .site-url {
    position: absolute; left: 372px; top: 372px; white-space: nowrap;
    font-family: "Montserrat", Arial, sans-serif; font-weight: 500; font-size: 20px; letter-spacing: 1px; color: var(--white);
  }

  .slide-dots { position: absolute; left: 925px; top: 380px; display: flex; gap: 6px; }
  .slide-dots span { width: 24px; height: 24px; border-radius: 50%; background: rgba(255,255,255,0.35); }
  .slide-dots span.active { background: rgba(255,255,255,0.8); }

  .brand-badge {
    position: absolute; left: 87px; top: 335px; width: 208px; height: 200px; background: var(--white);
    display: flex; flex-direction: column; align-items: center; justify-content: center; gap: 12px;
  }
  .brand-badge .mark { width: 70px; height: 70px; border-radius: 50%; background: var(--ink); }
  .brand-badge .name { font-size: 26px; color: var(--ink); text-transform: uppercase; letter-spacing: 1px; }
</style>
</head>
<body>
  <section class="cover">
    <div class="food-photo" role="img" aria-label="Close-up photo of a grilled steak on a white plate with rice and broccoli"></div>
    <div class="hours-panel"></div>
    <div class="contact-panel"></div>

    <h1 class="season-title">We’re Open</h1>
    <p class="season-months">March - October</p>
    <p class="hours-block hours-night">Open Friday and Saturday Night<br><span class="time">5:00 PM - 9:00 PM</span></p>
    <p class="hours-block hours-lunch">Lunch on Saturdays Only<br><span class="time">12:00 - 3:00 PM</span></p>

    <p class="offer-tag">$10 off second entree during march</p>

    <p class="contact-line contact-phone">
      <svg width="26" height="26" viewBox="0 0 26 26" aria-hidden="true"><circle cx="13" cy="13" r="13" fill="#c23a26"/><path d="M9 7c1 0 2 2.5 2 3s-1 1-1 1.5 2.5 3.5 3.5 3.5c.5 0 1-1 1.5-1s3 1 3 2-1.5 2.5-2.5 2.5C11 18.5 7.5 15 7.5 9.5 7.5 8.5 8 7 9 7z" fill="#fff"/></svg>
      555-213-8967
    </p>
    <p class="contact-line contact-address">
      <svg width="26" height="30" viewBox="0 0 26 30" aria-hidden="true"><path d="M13 1C6.5 1 2 5.5 2 11.5 2 19 13 29 13 29s11-10 11-17.5C24 5.5 19.5 1 13 1z" fill="#c23a26"/><circle cx="13" cy="11.5" r="4.5" fill="#fff"/></svg>
      <span>412 W. Cedar,<br>Pine Ridge,<br>Utah</span>
    </p>

    <div class="slide-dots"><span></span><span class="active"></span><span></span><span></span><span></span></div>

    <p class="site-url">www.thecopperkettlegrillhouse.example</p>
  </section>

  <div class="brand-badge">
    <span class="mark"></span>
    <span class="name">Copper Kettle</span>
  </div>
</body>
</html>
```